Visitenkarten-Design für das Business mit Gesundheit& Beauty
Zielgruppe
Ich bin selbständige Vertriebspartnerin von Vb. Die Visitenkarten sollen nicht zu verspielt wirken, eher geschäftlich. Dennoch könnte eine Verbindung zu den Bereichen Gesundheit & Beuuty dazukommen .
Hauptproduktmerkmal ist zum Beispiel die Aloe Vera, Naturprodukte.. mehr Infos auf : www.katrin-obelmoor.de
Instagram :kati_obelmoor
Eventuell könnte mein Slogan mit 'just more' noch einfließen, muss aber nicht. Bin für Ideen offen...
Aufgabenstellung
elegant und zeitlos, aber weich
Vielleicht eine goldene Aloe Vera irgendwie mit drauf?
Habe bei den dateien mal ein paar Screenshots hinzugefügt was ich recht schön fand

```html
<!DOCTYPE html>
<html lang="de">
<head>
<meta charset="utf-8">
<title>Katrin Obelmoor – Visitenkarte</title>
<link rel="stylesheet" href="https://fonts.googleapis.com/css2?family=Josefin+Sans:wght@300;400&family=Lora:wght@400;700&display=swap">
<style>
  :root {
    --page: #f1efec;
    --card: #0b0b0b;
    --gold-light: #f3d774;
    --gold: #c99a2e;
    --gold-deep: #8a5f12;
    --ink-light: #f4f1ea;
    --muted: #cfcac0;
  }
  * { margin: 0; padding: 0; box-sizing: border-box; }
  html, body { width: 1200px; height: 750px; overflow: hidden; }
  body {
    background: var(--page);
    display: flex;
    align-items: center;
    justify-content: center;
    gap: 60px;
  }
  .card {
    position: relative;
    width: 510px;
    height: 330px;
    background: var(--card);
    box-shadow: 0 18px 40px rgba(0,0,0,0.18);
  }
  /* contact side */
  .card-info .frame {
    position: absolute;
    inset: 22px;
    border: 1.5px solid var(--gold);
  }
  .brand {
    position: absolute;
    top: 58px;
    left: 0;
    right: 0;
    text-align: center;
  }
  .brand-name {
    font-family: "Josefin Sans", sans-serif;
    font-weight: 300;
    font-size: 27px;
    letter-spacing: 0.14em;
    color: var(--ink-light);
    text-transform: uppercase;
  }
  .brand-tagline {
    margin-top: 8px;
    font-family: "Josefin Sans", sans-serif;
    font-weight: 400;
    font-size: 9.5px;
    letter-spacing: 0.22em;
    color: var(--muted);
    text-transform: uppercase;
  }
  .divider {
    position: absolute;
    top: 142px;
    left: 92px;
    right: 92px;
    height: 1.5px;
    background: linear-gradient(90deg, var(--gold-deep), var(--gold-light), var(--gold));
  }
  .contact {
    position: absolute;
    top: 176px;
    left: 50px;
    right: 40px;
    display: flex;
    justify-content: space-between;
    font-family: "Lora", serif;
    font-size: 13px;
    line-height: 1.75;
    color: var(--ink-light);
  }
  .contact-col.right { margin-top: 44px; }
  .contact dt { display: inline; font-weight: 700; }
  .contact dd { display: inline; margin-left: 4px; }
  .contact .row { display: block; }
  /* pattern side */
  .card-pattern .ornament {
    position: absolute;
    inset: 20px;
    border: 1.5px solid var(--gold);
    background:
      radial-gradient(circle at 50% 50%, var(--gold-light) 0%, var(--gold) 28%, var(--gold-deep) 52%, #2a1d06 80%, #140e03 100%);
  }
</style>
</head>
<body>
  <section class="card card-info">
    <div class="frame"></div>
    <div class="brand">
      <div class="brand-name">Katrin Obelmoor</div>
      <div class="brand-tagline">Health, Beauty &amp; More</div>
    </div>
    <div class="divider"></div>
    <dl class="contact">
      <div class="contact-col left">
        <div class="row"><dt>Phone:</dt><dd>+49 170 5518274</dd></div>
        <div class="row"><dt>Email:</dt><dd>info@katrin-obelmoor.de</dd></div>
      </div>
      <div class="contact-col right">
        <div class="row"><dt>Address:</dt><dd>Talheim, Birkenweg 9</dd></div>
        <div class="row"><dt>Website:</dt><dd>www.katrin-obelmoor.de</dd></div>
      </div>
    </dl>
  </section>

  <section class="card card-pattern">
    <div class="ornament" role="img" aria-label="Goldenes Mandala-Ornament mit floralen Ranken auf Schwarz"></div>
  </section>
</body>
</html>
```